Business card

We are looking for a creative person to deigns our company business card.

Target Market(s)

College age student

Industry/Entity Type

Accommodation

Contact Information for Business Card

We want a fun, clean and sophisticated design. It should look good, but more importantly the information should be legible.

Font styles to use
Serif
Sans Serif
Other font styles liked:
• Open Sans ,

Colors
33a6d7

Requirements
Must have
• Must have a young and memorable message. Be legible.
• Our logo on the back on a solid blue , please find color and logo attached
• LodgeNestly.com on the back.
Nice to have
• I would like to have couple of different fonts on the LodgeNestly.com on the back of the cards with a solid blue.

```html
<!DOCTYPE html>
<html lang="en">
<head>
<meta charset="utf-8">
<title>LodgeNestly Business Card</title>
<link rel="stylesheet" href="https://fonts.googleapis.com/css2?family=Arimo:wght@700&family=Open+Sans:wght@400;600;700&display=swap">
<style>
  :root {
    --stage: #e8e8e8;
    --blue-light: #2aa3ee;
    --blue-mid: #1477c4;
    --blue-deep: #0a5a9c;
    --ink-blue: #1c5a8c;
    --brand-blue: #1b5f97;
    --ink: #333a40;
    --paper: #fbfbfb;
    --white: #ffffff;
  }
  * { box-sizing: border-box; margin: 0; padding: 0; }
  html, body {
    width: 1200px; height: 726px; overflow: hidden;
    background: var(--stage);
  }
  .canvas {
    position: relative; width: 1200px; height: 726px;
    display: flex; align-items: center; justify-content: center; gap: 60px;
  }
  .card {
    position: relative; width: 520px; height: 297px;
    border-radius: 2px;
    box-shadow: 0 6px 18px rgba(0,0,0,0.12);
    overflow: hidden;
  }
  /* Back side */
  .card-back {
    background: linear-gradient(160deg, var(--blue-light) 0%, var(--blue-mid) 50%, var(--blue-deep) 100%);
    display: flex; flex-direction: column; align-items: center; justify-content: center;
    color: var(--white);
  }
  .back-name {
    font-family: "Arimo", Arial, sans-serif; font-weight: 700;
    font-size: 46px; letter-spacing: -0.5px; line-height: 1;
  }
  .back-url {
    font-family: "Arimo", Arial, sans-serif; font-weight: 700;
    font-size: 14px; margin-top: 8px; letter-spacing: 0.3px;
  }
  /* Front side */
  .card-front {
    background: var(--paper);
    font-family: "Open Sans", Arial, sans-serif;
  }
  .brand {
    position: absolute; top: 92px; right: 36px;
    display: flex; align-items: center; gap: 8px;
  }
  .brand-square {
    width: 18px; height: 18px; background: var(--blue-light);
  }
  .brand-name {
    font-family: "Open Sans", Arial, sans-serif; font-weight: 700;
    font-size: 19px; color: var(--brand-blue);
  }
  .person {
    position: absolute; left: 40px; top: 102px;
  }
  .person-name {
    font-weight: 600; font-size: 21px; color: var(--ink-blue); line-height: 1.2;
  }
  .person-title {
    font-size: 12px; color: var(--ink); margin-top: 4px; margin-left: 12px;
  }
  .contact {
    position: absolute; left: 44px; bottom: 30px;
    list-style: none; font-size: 13px; color: var(--ink); line-height: 1.5;
  }
  .contact-line { display: flex; align-items: center; gap: 10px; }
  .contact-icon { width: 12px; height: 12px; flex: none; }
  .contact-icon-blank { width: 12px; flex: none; }
</style>
</head>
<body>
<main class="canvas">
  <section class="card card-back" aria-label="Card back">
    <div class="back-name">LodgeNestly</div>
    <div class="back-url">www.lodgenestly.com</div>
  </section>

  <section class="card card-front" aria-label="Card front">
    <div class="brand">
      <span class="brand-square"></span>
      <span class="brand-name">LodgeNestly</span>
    </div>
    <div class="person">
      <div class="person-name">Marcus Delgado</div>
      <div class="person-title">CEO &amp; Founder</div>
    </div>
    <ul class="contact">
      <li class="contact-line">
        <svg class="contact-icon" viewBox="0 0 12 12" aria-hidden="true"><path d="M2 1h2l1 3-1.5 1a7 7 0 0 0 3.5 3.5L8 7l3 1v2a1 1 0 0 1-1 1A9 9 0 0 1 1 2a1 1 0 0 1 1-1z" fill="var(--ink-blue)"/></svg>
        <span>1 (555) 014-2290</span>
      </li>
      <li class="contact-line">
        <svg class="contact-icon" viewBox="0 0 12 12" aria-hidden="true"><rect x="0.5" y="2" width="11" height="8" fill="var(--ink-blue)"/><path d="M0.5 2 6 6.5 11.5 2" fill="none" stroke="var(--white)" stroke-width="1"/></svg>
        <span>marcus@lodgenestly.com</span>
      </li>
      <li class="contact-line">
        <svg class="contact-icon" viewBox="0 0 12 12" aria-hidden="true"><circle cx="6" cy="6" r="5.5" fill="var(--ink-blue)"/><path d="M0.5 6h11M6 0.5v11M6 0.5c-3 3-3 8 0 11M6 0.5c3 3 3 8 0 11" fill="none" stroke="var(--white)" stroke-width="0.7"/></svg>
        <span>www.LodgeNestly.com</span>
      </li>
      <li class="contact-line">
        <span class="contact-icon-blank"></span>
        <span>118 Alder Row #204 Westfield, CA 90000</span>
      </li>
    </ul>
  </section>
</main>
</body>
</html>
```